Flyer-Design für Lumira Afghan Take Away
Zielgruppe
Gastrobetrieb mit Afghanischer Küche. Hauptangebot: Reisgerichte, Teigtaschen und Korma (Currygerichte). ZG: Studenten/Schüller, Ladenbesitzer und Passanten, da es sehr Zentral liegt
Aufgabenstellung
Öffnungszeiten:
MO: 11:30-14h
DI&MI: 11:30-14h/18h-20h
DO&FR: 11:30-14h/18h-21h
SA: 11:30-15h
SO: Geschlossen
INFO: www.lumira-imbiss.ch

```html
<!DOCTYPE html>
<html lang="de">
<head>
<meta charset="utf-8">
<title>Lumira Afghan Take Away – Flyer</title>
<link href="https://fonts.googleapis.com/css2?family=Montserrat:wght@500;600;700;800&family=Open+Sans:wght@400;600&display=swap" rel="stylesheet">
<style>
:root{
  --red:#c8202b;
  --red-dark:#8e2a27;
  --green:#2e5e2c;
  --green-text:#2f6b2d;
  --ink:#1d1d1b;
  --cream:#f4f1eb;
  --white:#ffffff;
  --card:#f6efe6;
}
*{box-sizing:border-box;margin:0;padding:0}
html,body{width:1200px;height:1200px;overflow:hidden;background:var(--white)}
body{position:relative;font-family:"Open Sans",Arial,sans-serif;color:var(--ink)}
.panel{position:absolute;top:72px;height:1030px;box-shadow:0 4px 14px rgba(0,0,0,.35);overflow:hidden}
.panel--menu{left:72px;width:514px;background:var(--cream)}
.panel--showcase{left:612px;width:516px;background:var(--white)}
.top-band{position:absolute;left:0;top:0;width:100%;height:60px}
.footer{position:absolute;left:0;bottom:0;width:100%;height:118px;background:var(--green);display:flex;align-items:center}
.footer__brand{width:120px;margin-left:34px;font-family:"Montserrat",sans-serif;font-weight:800;font-size:17px;line-height:1.05;color:var(--ink);text-align:center;text-transform:uppercase}
.footer__divider{width:0;height:82px;border-left:4px dotted var(--ink);margin:0 22px 0 20px}
.footer__address{display:flex;align-items:center;gap:12px;font-family:"Montserrat",sans-serif;font-weight:700;color:var(--ink)}
.footer__address svg{width:22px;height:32px}
.footer__street{font-size:25px;line-height:1}
.footer__city{font-size:20px;line-height:1.1}

.menu{position:absolute;left:84px;top:146px;width:338px}
.menu__heading{font-family:"Montserrat",sans-serif;font-weight:800;font-size:17px;color:var(--red);letter-spacing:.4px;display:flex;justify-content:space-between;align-items:flex-end;border-bottom:1px solid var(--red);padding-bottom:2px}
.menu__heading small{font-size:8px;font-weight:500;color:var(--ink)}
.dish{display:flex;border-bottom:1px solid var(--red);padding:3px 0 2px}
.dish__day{width:43px;font-family:"Montserrat",sans-serif;font-weight:800;font-size:16px;color:var(--red);line-height:1.2}
.dish__body{flex:1}
.dish__name{font-family:"Montserrat",sans-serif;font-weight:700;font-size:16px;line-height:1.2}
.dish__row{display:flex;justify-content:space-between;align-items:flex-end}
.dish__desc{font-size:8px;line-height:1.35;max-width:232px}
.dish__price{font-family:"Montserrat",sans-serif;font-weight:700;font-size:16px;line-height:1}
.daily{margin-top:26px}
.daily .dish__desc{max-width:260px}
.discount{margin-top:18px;text-align:right;font-size:8px;color:var(--red)}

.offer{position:absolute;left:16px;width:286px;height:194px;background:var(--card);border-radius:4px;overflow:hidden}
.offer__title{padding:12px 16px 0;font-family:"Montserrat",sans-serif;font-weight:700;font-size:14px;color:var(--red)}
.offer__desc{padding:2px 16px 0;font-size:8.6px;line-height:1.35;color:var(--red)}
.offer__photo{position:absolute;left:0;bottom:0;width:100%;height:118px;background:radial-gradient(ellipse at 50% 55%,#ffffff 0 32%,#e9dccb 60%,#c7a889 100%)}
.offer__price{position:absolute;right:12px;bottom:12px;width:56px;height:56px;border-radius:50%;background:var(--red);color:var(--white);font-family:Georgia,"Times New Roman",serif;font-style:italic;font-weight:700;font-size:21px;display:flex;align-items:center;justify-content:center}

.brand{position:absolute;left:390px;top:66px;width:126px;text-align:center;font-family:"Montserrat",sans-serif;font-weight:800;font-size:22px;line-height:1.05;color:var(--ink);text-transform:uppercase}
.brand span{display:block;font-size:10px}

.hours{position:absolute;left:214px;top:588px;width:460px;height:120px;transform:rotate(-90deg);font-family:"Montserrat",sans-serif;font-weight:800;font-size:17px;line-height:1.32;color:var(--green-text);white-space:nowrap}
.hours__title{color:var(--red);text-decoration:underline}
.hours b{color:var(--red);font-weight:800}
</style>
</head>
<body>

<section class="panel panel--menu">
  <svg class="top-band" viewBox="0 0 514 60" preserveAspectRatio="none"><path d="M0 0H514V44Q320 2 0 26Z" fill="var(--red-dark)"/></svg>

  <div class="menu">
    <h2 class="menu__heading">HAUSGEMACHTE MENÜS: <small>CHF</small></h2>

    <div class="dish"><div class="dish__day">MO:</div><div class="dish__body"><div class="dish__name">Lawang</div><div class="dish__row"><p class="dish__desc">Pouletbrustgeschn. in Kurkuma-Joghurt-Sauce und frischen Kräuter, dazu Brechbohnen Qorma und Basmatireis</p><span class="dish__price">14.50</span></div></div></div>
    <div class="dish"><div class="dish__day">DI:</div><div class="dish__body"><div class="dish__name">Qorma Tschalau</div><div class="dish__row"><p class="dish__desc">Basmatireis mit würzigem Rindfleisch, dazu Sabzi (gebratener Spinat)</p><span class="dish__price">14.50</span></div></div></div>
    <div class="dish"><div class="dish__day">MI:</div><div class="dish__body"><div class="dish__name">Kofta Tschalau</div><div class="dish__row"><p class="dish__desc">Basmatireis mit Kofta (Afgh. Meatballs), Dal (Linsen)</p><span class="dish__price">14.50</span></div></div></div>
    <div class="dish"><div class="dish__day">DO:</div><div class="dish__body"><div class="dish__name">Kabuli-Palau mit Pouletfleisch</div><div class="dish__row"><p class="dish__desc">Brauner Basmatireis mit Karottenstreifen, Rosinen, gekochtem Pouletfleisch und Qorme-e Gulpi (Blumenkohl an Tomatensauce)</p><span class="dish__price">14.50</span></div></div></div>
    <div class="dish"><div class="dish__day"></div><div class="dish__body"><div class="dish__name">Kabuli-Palau mit Lamm-Qorma</div><div class="dish__row"><p class="dish__desc">Brauner Basmati-Reis mit Karottenstr., Rosinen, Lamm-Qorma und Qorme-e Gulpi (Blumenkohl an Tomatens.)</p><span class="dish__price">16.50</span></div></div></div>
    <div class="dish"><div class="dish__day">FR:</div><div class="dish__body"><div class="dish__name">Mahi Tschalau</div><div class="dish__row"><p class="dish__desc">Basmatireis mit Fisch-Quorma und Qorme-e Sabzi (gebratener Spinat mit Bohnen)</p><span class="dish__price">14.50</span></div></div></div>
    <div class="dish"><div class="dish__day"></div><div class="dish__body"><div class="dish__name">Lawang</div><div class="dish__row"><p class="dish__desc">Pouletgeschn. in Kurkuma-Joghurt-Sauce und fr. Kräuter, Qorme-e Sabzi (gebr. Spinat mit Bohnen), Basmatireis</p><span class="dish__price">14.50</span></div></div></div>
    <div class="dish"><div class="dish__day">SA:</div><div class="dish__body"><div class="dish__name">Kabuli-Palau mit Pouletfleisch</div><div class="dish__row"><p class="dish__desc">Brauner Basmatireis mit Karottenstreifen, Rosinen, gekochtem Pouletfleisch und Qorme-e Gulpi (Blumenkohl an Tomatensauce)</p><span class="dish__price">14.50</span></div></div></div>
    <div class="dish"><div class="dish__day"></div><div class="dish__body"><div class="dish__name">Kabuli-Palau mit Lamm-Qorma</div><div class="dish__row"><p class="dish__desc">Brauner Basmati-Reis mit Karottenstreifen, Rosinen, Lamm-Qorma und Qorme-e Gulpi (Blumenkohl an Tomatensauce)</p><span class="dish__price">16.50</span></div></div></div>

    <div class="daily">
      <h2 class="menu__heading">TÄGLICHES ANGEBOT:</h2>
      <div class="dish"><div class="dish__body"><div class="dish__name">Mantu</div><div class="dish__row"><p class="dish__desc">Gedämpfte Rindhackfleischtaschen aus frischem Teig, dazu Tomatensauce mit gelben Erbsen und Joghurt-Minze-Sauce</p><span class="dish__price">14.00</span></div></div></div>
      <div class="dish"><div class="dish__body"><div class="dish__name">Ashak</div><div class="dish__row"><p class="dish__desc">Gedämpfte Lauchtaschen aus frischem Teig, dazu Tomatensauce mit gelben Erbsen und Joghurt-Minze-Sauce</p><span class="dish__price">14.00</span></div></div></div>
      <div class="dish"><div class="dish__body"><div class="dish__name">Chapli-Kabob im Taschenbrot</div><div class="dish__row"><p class="dish__desc">Gebratene Rindshacksteaks mit Gemüse, Salat, Chili-Koriander und Joghurt-Minze-Sauce</p><span class="dish__price">9.00</span></div></div></div>
      <div class="dish"><div class="dish__body"><div class="dish__name">2 Stk. Sambosa</div><div class="dish__row"><p class="dish__desc">Frittierte Kartoffel oder Gemüsetaschen, dazu Chili-Koriandersauce und Joghurt-Minze-Sauce</p><span class="dish__price">6.00</span></div></div></div>
      <div class="dish"><div class="dish__body"><div class="dish__name">Unsere Empfehlung: Lumira-Teller</div><div class="dish__row"><p class="dish__desc">Mix aus Tages-Menü und Teigtaschen</p><span class="dish__price">19.50</span></div></div></div>
    </div>
    <p class="discount">Wir haben auch Studenten-Rabatt!</p>
  </div>

  <footer class="footer">
    <div class="footer__brand">Lumira Afghan Take Away</div>
    <div class="footer__divider"></div>
    <div class="footer__address">
      <svg viewBox="0 0 22 32"><path d="M11 0C4.9 0 0 4.9 0 11c0 8 11 21 11 21s11-13 11-21C22 4.9 17.1 0 11 0Zm0 15.5a4.5 4.5 0 1 1 0-9 4.5 4.5 0 0 1 0 9Z" fill="var(--ink)"/></svg>
      <div><div class="footer__street">Lindenhofgasse 7</div><div class="footer__city">8001 Zürich</div></div>
    </div>
  </footer>
</section>

<section class="panel panel--showcase">
  <svg class="top-band" viewBox="0 0 516 60" preserveAspectRatio="none"><path d="M0 0H516V30Q200 -4 0 34Z" fill="var(--red-dark)"/></svg>

  <article class="offer" style="top:68px">
    <h3 class="offer__title">Mantu</h3>
    <p class="offer__desc">Gedämpfte Rindhackfleischtaschen aus frischem Teig, dazu Tomatensauce mit gelben Erbsen und Joghurt-Minze-Sauce</p>
    <div class="offer__photo" role="img" aria-label="Foto: Mantu-Teigtaschen mit Tomatensauce in weisser Schale"></div>
    <div class="offer__price">14.-</div>
  </article>
  <article class="offer" style="top:276px">
    <h3 class="offer__title">Ashak</h3>
    <p class="offer__desc">Gedämpfte Lauchtaschen aus frischem Teig, dazu Tomatensauce mit gelben Erbsen und Joghurt-Minze-Sauce</p>
    <div class="offer__photo" role="img" aria-label="Foto: Ashak-Lauchtaschen mit Joghurt und Tomatensauce"></div>
    <div class="offer__price">14.-</div>
  </article>
  <article class="offer" style="top:484px">
    <h3 class="offer__title">Chapli-Kabob im Taschenbrot</h3>
    <p class="offer__desc">Gebratene Rindshacksteaks mit Gemüse, Salat, Chili-Koriander und Joghurt-Minze-Sauce</p>
    <div class="offer__photo" role="img" aria-label="Foto: Chapli-Kabob im Taschenbrot"></div>
    <div class="offer__price">9.-</div>
  </article>
  <article class="offer" style="top:692px">
    <h3 class="offer__title">Sambosa 2 Stk.</h3>
    <p class="offer__desc">Frittierte Kartoffel oder Gemüsetaschen, dazu Chili-Koriandersauce und Joghurt-Minze-Sauce</p>
    <div class="offer__photo" role="img" aria-label="Foto: zwei Sambosa mit Dip-Saucen"></div>
    <div class="offer__price">6.-</div>
  </article>

  <div class="brand">Lumira<span>Afghan Take Away</span></div>

  <div class="hours">
    <div class="hours__title">Öffnungszeiten:</div>
    <div><b>MO:</b> 11:30-14h &nbsp;- &nbsp;<b>DI&amp;MI:</b> 11:30-14h/18h-20h</div>
    <div><b>DO&amp;FR:</b> 11:30-14h/18h-21h</div>
    <div><b>SA:</b> 11:30-15h &nbsp;- &nbsp;<b>SO:</b> Geschlossen</div>
    <div>www.lumira-imbiss.ch</div>
  </div>

  <footer class="footer">
    <div class="footer__brand">Lumira Afghan Take Away</div>
    <div class="footer__divider"></div>
    <div class="footer__address">
      <svg viewBox="0 0 22 32"><path d="M11 0C4.9 0 0 4.9 0 11c0 8 11 21 11 21s11-13 11-21C22 4.9 17.1 0 11 0Zm0 15.5a4.5 4.5 0 1 1 0-9 4.5 4.5 0 0 1 0 9Z" fill="var(--ink)"/></svg>
      <div><div class="footer__street">Lindenhofgasse 7</div><div class="footer__city">8001 Zürich</div></div>
    </div>
  </footer>
</section>

</body>
</html>
```